Design 3 Banners, 940 x 480, for the website of a cleaning company landing page

Please use this for colour scheme ideas and inspiration (these are fylers I had designed) : https://www.gigboard.example/contest/Design-a-Flyer-for-Bright-and-Brisk-Cleaning-58193.html

I require 3 banners, sized 940 x 480 , for the home page of my website www.BrightandBrisk.example.

they will replace the current slideshow of banners.(low quality list of services and image of a tidy house)

I would like the 3 of them to include the following information, distributed evenly across the 3 banners;

-Book in 60 seconds, Online, Easy
-Teams on 2 for double the clean
-No contracts
-Simple flat-rate pricing
-Fully insured
-On-time service
-We also support charities

********-Secure payment through coinvault/128-bit encryption/256 bit encryption (currently using coinvault, but want to build trust)

********-100% guarantee sign!

```html
<!DOCTYPE html>
<html lang="en">
<head>
<meta charset="utf-8">
<title>Bright and Brisk Cleaning – Banner</title>
<link rel="stylesheet" href="https://fonts.googleapis.com/css2?family=Russo+One&family=Roboto:wght@700&display=swap">
<style>
  :root {
    --panel-dark: #141414;
    --panel-mid: #2b2b2b;
    --row-light: #4a4a4a;
    --row-dark: #1d1d1d;
    --feature-blue: #3f86d8;
    --outline-white: #ffffff;
    --icon-white: #f2f2f2;
    --room-cream: #efe6d8;
    --room-warm: #d9c7ae;
    --room-light: #fbf8f2;
    --brand-blue: #1e4f8f;
    --seal-gold: #e0b21c;
    --seal-dark: #1a1a1a;
  }
  * { margin: 0; padding: 0; box-sizing: border-box; }
  html, body { width: 1200px; height: 613px; overflow: hidden; background: #fff; }
  .banner { position: relative; width: 1200px; height: 613px; overflow: hidden; font-family: "Roboto", Arial, sans-serif; }
  .backdrop { position: absolute; inset: 0; }
  .feature-list { position: absolute; left: 0; top: 58px; list-style: none; }
  .feature {
    display: flex; align-items: center;
    width: 436px; height: 43px; margin-bottom: 18px;
    background: linear-gradient(to bottom, var(--row-light), var(--row-dark));
    border-top: 1px solid #5c5c5c;
  }
  .feature-icon {
    flex: 0 0 60px; width: 60px; height: 100%;
    display: flex; align-items: center; justify-content: center;
    background: rgba(0,0,0,0.25);
  }
  .feature-icon svg { width: 30px; height: 30px; fill: none; stroke: var(--icon-white); stroke-width: 2; stroke-linecap: round; stroke-linejoin: round; }
  .feature-text {
    margin-left: 16px;
    font-family: "Russo One", Impact, sans-serif;
    font-style: italic;
    font-size: 21px;
    color: var(--feature-blue);
    -webkit-text-stroke: 1px var(--outline-white);
    paint-order: stroke fill;
    text-shadow: 1px 1px 0 #fff, -1px -1px 0 #fff;
    white-space: nowrap;
  }
  .secure-payment { position: absolute; left: 22px; top: 510px; display: flex; align-items: center; gap: 18px; }
  .secure-payment svg { width: 56px; height: 56px; flex: 0 0 56px; }
  .secure-text { color: #fff; font-size: 21px; font-weight: 700; white-space: nowrap; }
  .brand { position: absolute; left: 770px; top: 522px; display: flex; align-items: center; gap: 10px; }
  .brand-dot { width: 22px; height: 22px; border-radius: 50%; background: var(--brand-blue); }
  .brand-name { font-size: 28px; font-weight: 700; color: var(--brand-blue); white-space: nowrap; }
  .guarantee-seal { position: absolute; left: 1050px; top: 480px; width: 122px; height: 122px; border-radius: 50%;
    background: radial-gradient(circle, var(--seal-gold) 58%, var(--seal-dark) 60%, var(--seal-dark) 66%, var(--seal-gold) 68%); }
</style>
</head>
<body>
<div class="banner">
  <svg class="backdrop" width="1200" height="613" viewBox="0 0 1200 613">
    <defs>
      <linearGradient id="room-tones" x1="0" y1="0" x2="1" y2="1">
        <stop offset="0" stop-color="var(--room-light)"/>
        <stop offset="0.55" stop-color="var(--room-cream)"/>
        <stop offset="1" stop-color="var(--room-warm)"/>
      </linearGradient>
      <linearGradient id="panel-tones" x1="0" y1="0" x2="1" y2="1">
        <stop offset="0" stop-color="var(--panel-mid)"/>
        <stop offset="1" stop-color="var(--panel-dark)"/>
      </linearGradient>
    </defs>
    <rect x="0" y="0" width="1200" height="613" fill="url(#panel-tones)"/>
    <polygon points="562,0 1200,0 1200,613 562,613 440,306" fill="url(#room-tones)" role="img" aria-label="Bright modern living room with cream armchairs, glass coffee table, plant, sofa and wall-mounted TV"/>
  </svg>

  <ul class="feature-list">
    <li class="feature"><span class="feature-icon"><svg viewBox="0 0 30 30"><rect x="4" y="5" width="22" height="15" rx="1"/><path d="M11 25h8M15 20v5M9 11h12M9 15h8"/></svg></span><span class="feature-text">Book in 60 Seconds, Online, Easy</span></li>
    <li class="feature"><span class="feature-icon"><svg viewBox="0 0 30 30"><path d="M20 8a5 5 0 0 0-9 3v12M8 16h9M8 24h14"/></svg></span><span class="feature-text">Simple Flat Rate Pricing</span></li>
    <li class="feature"><span class="feature-icon"><svg viewBox="0 0 30 30"><rect x="9" y="4" width="15" height="20"/><path d="M12 10h9M12 14h9"/><path d="M4 18l7 7M11 18l-7 7" stroke="#e23a2a"/></svg></span><span class="feature-text">No Contracts</span></li>
    <li class="feature"><span class="feature-icon"><svg viewBox="0 0 30 30"><path d="M6 14h5v12H6zM11 14l5-9c2 0 3 1 3 3l-1 5h6c2 0 3 2 2 4l-2 7c-1 2-2 2-3 2h-10"/></svg></span><span class="feature-text">Fully Insured</span></li>
    <li class="feature"><span class="feature-icon"><svg viewBox="0 0 30 30"><circle cx="16" cy="11" r="7"/><path d="M16 7v4l3 2M3 22c4-3 8-2 11 0h9"/></svg></span><span class="feature-text">On-time Service</span></li>
    <li class="feature"><span class="feature-icon"><svg viewBox="0 0 30 30"><circle cx="8" cy="5" r="2.5"/><circle cx="22" cy="5" r="2.5"/><path d="M8 9v9l-3 8M8 18l3 8M22 9v9l-3 8M22 18l3 8M8 12h14"/></svg></span><span class="feature-text">Teams of 2 for Double the Clean</span></li>
    <li class="feature"><span class="feature-icon"><svg viewBox="0 0 30 30"><circle cx="16" cy="6" r="3"/><path d="M12 16h8M16 10v6M3 22c4-3 8-2 11 0h9"/></svg></span><span class="feature-text">we also support charities</span></li>
  </ul>

  <div class="secure-payment">
    <svg viewBox="0 0 56 56"><path d="M18 26v-8a10 10 0 0 1 20 0v8" fill="none" stroke="#9a9a9a" stroke-width="5"/><rect x="12" y="26" width="32" height="24" rx="3" fill="#c9a23a"/><circle cx="28" cy="37" r="3" fill="#3a2e10"/></svg>
    <span class="secure-text">Secure Payment Through coinvault</span>
  </div>

  <div class="brand">
    <span class="brand-dot"></span>
    <span class="brand-name">Bright and Brisk</span>
  </div>

  <div class="guarantee-seal" role="img" aria-label="Satisfaction guarantee seal"></div>
</div>
</body>
</html>
```